Property investment company needs a letterhead design!

We are a new residential and commercial property investment company. Name of the company is Morvesta Group, LLC. We have a new logo and now we need letterhead! We prefer to have a professional and upscale appearance. We don't have any fixed requirements, so be creative! Thank you for considering this project. We are so excited to see what happens!

Target Market(s)

Professional

Industry/Entity Type

Real Estate Development

```html
<!DOCTYPE html>
<html lang="en">
<head>
<meta charset="utf-8">
<title>Morvesta Real Estate – Letterhead</title>
<link rel="stylesheet" href="https://fonts.googleapis.com/css2?family=Archivo+Black&family=Archivo:wght@600&family=Roboto+Condensed:wght@400&family=Montserrat:wght@500&family=Open+Sans:wght@400&family=Source+Sans+3:wght@400&display=swap">
<style>
  :root {
    --navy: #00008f;
    --sky: #2680ff;
    --mist: #cccccc;
    --paper: #ffffff;
    --ink: #111111;
  }
  html, body {
    margin: 0;
    padding: 0;
    width: 1200px;
    height: 1000px;
    overflow: hidden;
    background: var(--paper);
  }
  .letterhead {
    display: block;
    width: 1200px;
    height: 1000px;
  }
  .panel-mist { fill: var(--mist); }
  .panel-sky { fill: var(--sky); }
  .band-navy { fill: var(--navy); }
  .frame-line { stroke: var(--navy); stroke-width: 1; fill: none; }
  .brand-name {
    font-family: "Archivo Black", "Arial Black", sans-serif;
    font-size: 88px;
    fill: var(--navy);
  }
  .brand-tagline {
    font-family: "Archivo", Arial, sans-serif;
    font-weight: 600;
    font-size: 42px;
    fill: var(--navy);
  }
  .company-mark {
    font-family: "Archivo", Arial, sans-serif;
    font-weight: 600;
    font-size: 28px;
    fill: var(--navy);
  }
  .company-mark-dot { fill: var(--navy); }
  .contact-condensed {
    font-family: "Roboto Condensed", "Arial Narrow", sans-serif;
    font-size: 22px;
    fill: var(--paper);
  }
  .contact-phone {
    font-family: "Montserrat", "Century Gothic", sans-serif;
    font-weight: 500;
    font-size: 19px;
    fill: var(--paper);
  }
  .section-label {
    font-family: "Open Sans", Arial, sans-serif;
    font-size: 22px;
    fill: var(--paper);
  }
  .project-list {
    font-family: "Open Sans", Arial, sans-serif;
    font-size: 16px;
    fill: var(--ink);
  }
  .address-line {
    font-family: "Source Sans 3", "Myriad Pro", sans-serif;
    font-size: 24px;
    fill: var(--navy);
  }
</style>
</head>
<body>
<svg class="letterhead" viewBox="0 0 1200 1000" xmlns="http://www.w3.org/2000/svg" aria-label="Morvesta Real Estate letterhead">
  <!-- header panels -->
  <polygon class="panel-mist" points="0,0 297,0 334,45 250,282 0,257"/>
  <polygon class="band-navy" points="297,0 914,0 878,44 334,45"/>
  <polygon class="panel-sky" points="914,0 1200,0 1200,257 963,280 878,44"/>
  <polyline class="frame-line" points="334,45 250,282"/>
  <polyline class="frame-line" points="878,44 963,280"/>

  <!-- side ribbons -->
  <polygon class="band-navy" points="0,257 250,282 0,327"/>
  <polygon class="band-navy" points="1200,257 963,280 1200,322"/>

  <!-- header wave -->
  <path class="band-navy" d="M250,282 C275,255 320,247 362,247 C450,247 550,256 631,265 L846,265 L963,280 Z"/>

  <!-- body frame -->
  <line class="frame-line" x1="250" y1="282" x2="963" y2="280"/>
  <line class="frame-line" x1="250" y1="282" x2="250" y2="1000"/>
  <line class="frame-line" x1="963" y1="280" x2="963" y2="1000"/>
  <line class="frame-line" x1="250" y1="949" x2="963" y2="949"/>

  <!-- company name in the mark position -->
  <circle class="company-mark-dot" cx="152" cy="88" r="14"/>
  <text class="company-mark" x="152" y="145" text-anchor="middle">MORVESTA</text>
  <text class="company-mark" x="152" y="178" text-anchor="middle" style="font-size:18px">GROUP, LLC</text>

  <!-- masthead -->
  <text class="brand-name" x="318" y="190" textLength="595" lengthAdjust="spacingAndGlyphs">MORVESTA</text>
  <text class="brand-tagline" x="655" y="236" textLength="258" lengthAdjust="spacingAndGlyphs">Real Estate</text>

  <!-- contact details -->
  <text class="contact-condensed" x="475" y="35" textLength="246" lengthAdjust="spacingAndGlyphs">Email: MorvestaLLC@mailbox.com</text>
  <text class="contact-phone" x="938" y="154" textLength="250" lengthAdjust="spacingAndGlyphs">Phone: (555) 214-0376</text>
  <text class="contact-condensed" x="936" y="185" textLength="252" lengthAdjust="spacingAndGlyphs">Website: www.MorvestaLLC.com</text>

  <!-- section labels -->
  <text class="section-label" transform="translate(15,313) rotate(-9)">Residential:</text>
  <text class="section-label" transform="translate(1061,285) rotate(9)" textLength="124" lengthAdjust="spacingAndGlyphs">Commercial:</text>

  <!-- project lists -->
  <text class="project-list" x="22" y="365">
    <tspan x="22">Porject 1</tspan>
    <tspan x="22" dy="21.6">Project 2</tspan>
    <tspan x="22" dy="21.6">Project 3</tspan>
    <tspan x="22" dy="21.6">Project 4</tspan>
    <tspan x="22" dy="21.6">Project 5</tspan>
  </text>
  <text class="project-list" x="993" y="365">
    <tspan x="993">Porject 1</tspan>
    <tspan x="993" dy="21.6">Project 2</tspan>
    <tspan x="993" dy="21.6">Project 3</tspan>
    <tspan x="993" dy="21.6">Project 4</tspan>
    <tspan x="993" dy="21.6">Project 5</tspan>
  </text>

  <!-- footer address -->
  <text class="address-line" x="351" y="979" textLength="511" lengthAdjust="spacingAndGlyphs">Address: 1846 N. Alder Ave. Pine Hollow, MI 49012</text>
</svg>
</body>
</html>
```